Simple, Professional and neat business card design for Vendralo Inc.

We're looking to re-vamp our business card design. We're a supplier of innovative feed ingredients for the North American animal agriculture industry. We are located in Lucknow, Ontario, Canada and our flagship product is a product that prevents milk fever in dairy cows when the calve, it is fed before calving and is very effective compared to other alternatives available on the market today.

Our company has Danish roots and we import all of our product from our Danish partner/manufacturer in Denmark. We like our design to embrace high professionalism while remaining neat and simple.

Target Market(s)

B2B, Feed Mills, Veterinary Clinics, Large integrators/producers,

Industry/Entity Type

Agribusiness

Contact Information for Business Card

We like the rounded corners because they make the card easy to sit in a wallet and not many use it so it makes the card stand out, just possibly something to take account for during the design.

As you can also see on the sliders below, looking for a that simple but proffesional scandinavian design.

Requirements
Nice to have
• Rounded corners
Should not have
• Too vibrant

```html
<!DOCTYPE html>
<html lang="en">
<head>
<meta charset="UTF-8">
<title>Vendralo Inc. — Business Card</title>
<link rel="stylesheet" href="https://fonts.googleapis.com/css2?family=Lato:wght@400;700&display=swap">
<style>
  :root {
    --page-bg: #e6e8eb;
    --card-bg: #ffffff;
    --brand-blue: #2a7cc7;
    --brand-blue-deep: #1f6db5;
    --swoosh-grey: #8e9094;
    --text-dark: #2b2b2b;
    --text-muted: #6a6a6a;
  }
  * { box-sizing: border-box; margin: 0; padding: 0; }
  html, body { width: 1200px; height: 900px; overflow: hidden; }
  body {
    background: var(--page-bg);
    font-family: "Lato", sans-serif;
    display: flex;
    flex-direction: column;
    align-items: center;
    justify-content: center;
    gap: 50px;
  }
  .card {
    position: relative;
    width: 600px;
    height: 343px;
    background: var(--card-bg);
    border-radius: 20px;
    overflow: hidden;
    box-shadow: 0 4px 14px rgba(0,0,0,0.12);
  }
  .card-swoosh { position: absolute; inset: 0; width: 100%; height: 100%; }

  /* front */
  .front-mark {
    position: absolute;
    left: 0; right: 0; top: 110px;
    display: flex; align-items: center; justify-content: center; gap: 14px;
  }
  .mark-dot {
    width: 26px; height: 26px; border-radius: 50%;
    background: var(--brand-blue);
  }
  .front-name {
    font-weight: 700; font-size: 40px; letter-spacing: 1px;
    color: var(--brand-blue);
  }
  .front-web {
    position: absolute; left: 0; right: 0; top: 190px;
    text-align: center;
    font-size: 14px; letter-spacing: 7px;
    color: var(--text-muted);
  }

  /* back */
  .back-header {
    position: absolute; left: 34px; top: 34px;
    display: flex; align-items: center; gap: 12px;
  }
  .mark-dot.small { width: 22px; height: 22px; }
  .company-name {
    font-weight: 700; font-size: 32px; letter-spacing: 0.5px;
    color: var(--brand-blue);
  }
  .person {
    position: absolute; right: 34px; top: 38px; text-align: right;
  }
  .person-name {
    font-weight: 700; font-size: 16px; color: var(--brand-blue);
    letter-spacing: 0.3px;
  }
  .person-title { font-size: 12px; color: var(--text-dark); margin-top: 2px; }
  .person-email {
    display: block; margin-top: 14px;
    font-size: 13px; font-weight: 700; color: var(--brand-blue); text-decoration: none;
  }
  .contact-list {
    position: absolute; left: 40px; top: 150px;
    display: grid; grid-template-columns: auto auto; column-gap: 12px; row-gap: 6px;
    font-size: 14px;
  }
  .contact-label {
    font-weight: 700; color: var(--brand-blue);
    border-bottom: 1px solid var(--brand-blue); padding-bottom: 1px;
  }
  .contact-value { color: var(--text-dark); }
</style>
</head>
<body>

  <section class="card card-front">
    <div class="front-mark">
      <span class="mark-dot"></span>
      <span class="front-name">Vendralo Inc.</span>
    </div>
    <p class="front-web">www.vendralo.com</p>
    <svg class="card-swoosh" viewBox="0 0 600 343" preserveAspectRatio="none" aria-hidden="true">
      <path d="M215 320 C 400 290 530 210 600 95 L600 110 C 530 222 400 302 215 320 Z" fill="var(--swoosh-grey)"/>
      <path d="M0 343 L0 330 C 270 318 490 245 600 125 L600 343 Z" fill="var(--brand-blue)"/>
    </svg>
  </section>

  <section class="card card-back">
    <div class="back-header">
      <span class="mark-dot small"></span>
      <h1 class="company-name">VENDRALO INC.</h1>
    </div>
    <div class="person">
      <p class="person-name">MIKKEL SORENSEN</p>
      <p class="person-title">Managing Director</p>
      <a class="person-email" href="mailto:mikkel@vendralo.com">mikkel@vendralo.com</a>
    </div>
    <div class="contact-list">
      <span class="contact-label">Mobile:</span><span class="contact-value">555-310-0142</span>
      <span class="contact-label">Office:</span><span class="contact-value">555-284-0167</span>
      <span class="contact-label">Fax:</span><span class="contact-value">555-284-0199</span>
      <span class="contact-label">Toll Free:</span><span class="contact-value">800-555-0136</span>
    </div>
    <svg class="card-swoosh" viewBox="0 0 600 343" preserveAspectRatio="none" aria-hidden="true">
      <path d="M215 320 C 400 290 530 210 600 95 L600 110 C 530 222 400 302 215 320 Z" fill="var(--swoosh-grey)"/>
      <path d="M0 343 L0 330 C 270 318 490 245 600 125 L600 343 Z" fill="var(--brand-blue)"/>
    </svg>
  </section>

</body>
</html>
```